Quality winery located in Northern California desires wine bottle label redesign

We want to redesign our Drifting Comet brand label. We have been making this wine for 24 years, it is our popular priced point wine ($15.00 a bottle). We would like to see a Drifting Comet as part of the label motif. Refer to our website to view the current version and the explanation of the name Drifting Comet as seen on the back label. The winemakers name is Bartholomew Ainsley Crowder, the website is www.crowdercellars.example.
We are looking for a front label only, back will remain basically the same.
Updates

Project Deadline Extended
Reason: We just havn't reached a consensus yet.

Project Deadline Extended
Reason: We have had very few responses from distributors, we would like to have more feedback.

Project Deadline Extended
Reason: Apologize for another extension, we still have not heard back from many of our distributors, will contact them this week.

We wanted to thank everyone for investing time and thought into our label design project. This has been a pleasure working with sketch forum.

Target Market(s)

Buying age 21 -45, buyers of wines in the retail market. Has to stand out on the shelf.

Colors

Designer to choose colors to be used in the design.

Requirements
Must have
• Drifting Comet displayed
Should not have
• Varietal cannot be in script, must be in block letters.

```html
<!DOCTYPE html>
<html lang="en">
<head>
<meta charset="utf-8">
<title>Drifting Comet Syrah – Front Label</title>
<link href="https://fonts.googleapis.com/css2?family=Tangerine:wght@400&family=Open+Sans:wdth,wght@75..100,300..600&display=swap" rel="stylesheet">
<style>
  :root {
    --page: #ffffff;
    --night: #07060f;
    --violet: #5a3fc4;
    --magenta: #8a2bb8;
    --cyan: #2f8fd8;
    --band: #26253f;
    --band-line: #2e2b55;
    --ink: #f2f0ee;
  }
  * { margin: 0; padding: 0; box-sizing: border-box; }
  html, body {
    width: 1200px;
    height: 2233px;
    overflow: hidden;
    background: var(--page);
  }
  .canvas {
    position: relative;
    width: 1200px;
    height: 2233px;
    background: var(--page);
  }
  .label {
    position: absolute;
    left: 94px;
    top: 0;
    width: 1018px;
    height: 2233px;
    overflow: hidden;
  }
  .label-art, .label-band {
    position: absolute;
    left: 0;
    top: 0;
    width: 1018px;
    height: 2233px;
  }
  .brand-name {
    position: absolute;
    left: 70px;
    top: 1010px;
    width: 910px;
    font-family: "Tangerine", cursive;
    font-weight: 400;
    font-size: 200px;
    line-height: 1;
    color: var(--ink);
    white-space: nowrap;
    text-align: center;
  }
  .varietal {
    position: absolute;
    right: 52px;
    top: 1218px;
    font-family: "Open Sans", sans-serif;
    font-weight: 400;
    font-size: 62px;
    letter-spacing: 1px;
    line-height: 1;
    color: var(--ink);
  }
  .appellation {
    position: absolute;
    right: 52px;
    top: 1296px;
    font-family: "Open Sans", sans-serif;
    font-stretch: 80%;
    font-weight: 400;
    font-size: 34px;
    line-height: 1;
    color: var(--ink);
  }
</style>
</head>
<body>
<main class="canvas">
  <section class="label">
    <svg class="label-art" viewBox="0 0 1018 2233" role="img" aria-label="Abstract fractal artwork of glowing violet, blue and magenta streaks and lightning on a black night sky">
      <defs>
        <radialGradient id="glow-upper" cx="0.45" cy="0.3" r="0.6">
          <stop offset="0" stop-color="var(--violet)" stop-opacity="0.75"/>
          <stop offset="0.45" stop-color="var(--magenta)" stop-opacity="0.3"/>
          <stop offset="1" stop-color="var(--night)" stop-opacity="0"/>
        </radialGradient>
        <radialGradient id="glow-lower" cx="0.6" cy="0.72" r="0.55">
          <stop offset="0" stop-color="var(--violet)" stop-opacity="0.7"/>
          <stop offset="0.5" stop-color="var(--cyan)" stop-opacity="0.2"/>
          <stop offset="1" stop-color="var(--night)" stop-opacity="0"/>
        </radialGradient>
      </defs>
      <rect width="1018" height="2233" fill="var(--night)"/>
      <rect width="1018" height="1000" fill="url(#glow-upper)"/>
      <rect y="1300" width="1018" height="933" fill="url(#glow-lower)"/>
    </svg>

    <svg class="label-band" viewBox="0 0 1018 2233" aria-hidden="true">
      <polygon points="0,866 1018,690 1018,704 0,880" fill="var(--band-line)"/>
      <polygon points="0,910 1018,744 1018,1490 0,1300" fill="var(--band)"/>
      <polygon points="0,1340 1018,1530 1018,1544 0,1354" fill="var(--band-line)"/>
    </svg>

    <h1 class="brand-name">Drifting Comet</h1>
    <p class="varietal">SYRAH</p>
    <p class="appellation">LAKE COUNTRY</p>
  </section>
</main>
</body>
</html>
```